Venture Keystone - Client Appreciation Party Invitation and Poster

We need a printable invitation, a version of the same invitation that can be emailed out, and also a Poster of the invitation for our annual client appreciation party.

The location is called: The Lanternhouse. Here is a link to the location: https://www.thelanternhousevenue.example/

We like their font and their little logo that you see when you log onto this page. But we'd love to see creatively what you can come up with.

This party is for our clients who are interior designers and owners in the Hospitality industry. Here are the details which need to be included in the invitation:

Location: The Lanternhouse - 482 W Brindle Ave. Chicago IL 60614
Date/Time: Thursday August 23rd - 5:30-9:00pm
RSVP: Please RSVP to: gathering@venturekeystone.example

Then our Sponsors Logos need to be included on the bottom: I have uploaded those logos here as well as our Logo and a copy of the invitation we did for last year's party so you can see sort of what we've done in the past.

For the poster - we typically do a version of the invitation (see uploaded example of last year's poster) with the sponsor logos and the overall theme of the invitation just a bit simplified by removing the date/time/location info. We need this in a printable format which can be blown up to a 24x30 poster size.

Requirements
Must have
• use 2 to 3 colors only.
• logos of sponsors can be of the same color.

```html
<!DOCTYPE html>
<html lang="en">
<head>
<meta charset="utf-8">
<title>Venture Keystone Weekend Warm Up – Client Appreciation Event</title>
<link href="https://fonts.googleapis.com/css2?family=Cormorant+Garamond:wght@500;600&family=Montserrat:wght@400&family=Oswald:wght@600&display=swap" rel="stylesheet">
<style>
  :root {
    --ink-blue: #1f2f9a;
    --ink-black: #1c1c1c;
    --leaf-green: #8cc152;
    --paper: #f8f7f3;
    --white: #ffffff;
  }
  html, body {
    margin: 0;
    padding: 0;
    overflow: hidden;
    background: var(--paper);
  }
  .poster {
    position: relative;
    width: 857px;
    height: 1200px;
    overflow: hidden;
    background: var(--paper);
    font-family: "Cormorant Garamond", Georgia, serif;
  }
  .background-pattern {
    position: absolute;
    inset: 0;
    background: var(--paper);
  }
  .frame {
    position: absolute;
    border: 3px solid var(--ink-blue);
  }
  .frame--outer { left: 64px; top: 57px; width: 730px; height: 1080px; }
  .frame--inner { left: 71px; top: 64px; width: 716px; height: 1066px; border-width: 1px; }
  .corner-ornament {
    position: absolute;
    width: 160px;
    height: 136px;
    background: radial-gradient(circle, #c9cfee 0%, #e8eaf5 60%, var(--paper) 100%);
  }
  .corner-ornament--top-right { left: 664px; top: 32px; }
  .corner-ornament--bottom-left { left: 36px; top: 1016px; }

  .host {
    position: absolute;
    top: 98px;
    left: 0;
    width: 100%;
    text-align: center;
    font-family: "Montserrat", Arial, sans-serif;
    font-size: 16px;
    letter-spacing: 0.28em;
    color: var(--ink-black);
  }
  .title {
    position: absolute;
    left: 0;
    width: 100%;
    margin: 0;
    text-align: center;
    font-weight: 500;
    line-height: 1;
    letter-spacing: 0.01em;
  }
  .title--weekend { top: 124px; font-size: 84px; color: var(--ink-blue); }
  .title--warm-up { top: 194px; font-size: 84px; color: var(--ink-black); }

  .venue-wreath {
    position: absolute;
    left: 172px;
    top: 280px;
    width: 516px;
    height: 536px;
    border-radius: 50%;
    background: radial-gradient(circle, #c7e2a6 0%, #a6cf78 45%, rgba(166, 207, 120, 0.35) 68%, rgba(248, 247, 243, 0) 74%);
  }
  .venue-badge {
    position: absolute;
    left: 258px;
    top: 380px;
    width: 340px;
    height: 340px;
    box-sizing: border-box;
    border-radius: 50%;
    border: 2px solid var(--leaf-green);
    background: var(--white);
    display: flex;
    flex-direction: column;
    align-items: center;
    justify-content: center;
    color: var(--ink-black);
    text-align: center;
  }
  .venue-name {
    font-size: 30px;
    font-weight: 600;
    letter-spacing: 0.14em;
    text-transform: uppercase;
    line-height: 1.15;
  }
  .venue-address {
    margin-top: 14px;
    font-size: 20px;
    font-weight: 600;
    letter-spacing: 0.16em;
    text-transform: uppercase;
  }

  .event-type {
    position: absolute;
    top: 826px;
    left: 0;
    width: 100%;
    margin: 0;
    text-align: center;
    font-family: "Oswald", "Arial Narrow", sans-serif;
    font-weight: 600;
    font-size: 60px;
    line-height: 1;
    color: var(--ink-blue);
    letter-spacing: -0.005em;
  }

  .sponsors {
    position: absolute;
    top: 918px;
    left: 110px;
    width: 630px;
    display: grid;
    grid-template-columns: repeat(3, 1fr);
    grid-template-rows: 60px 70px;
    align-items: center;
    justify-items: center;
    margin: 0;
    padding: 0;
    list-style: none;
  }
  .sponsor {
    display: flex;
    align-items: center;
    gap: 8px;
    font-size: 25px;
    font-weight: 600;
    color: var(--ink-black);
    white-space: nowrap;
  }
  .sponsor-mark {
    width: 14px;
    height: 14px;
    border: 2px solid var(--ink-black);
    border-radius: 3px;
  }
</style>
</head>
<body>
  <main class="poster">
    <div class="background-pattern" role="img" aria-label="Faint damask pattern background"></div>

    <div class="frame frame--outer"></div>
    <div class="frame frame--inner"></div>
    <div class="corner-ornament corner-ornament--top-right" role="img" aria-label="Blue filigree corner ornament"></div>
    <div class="corner-ornament corner-ornament--bottom-left" role="img" aria-label="Blue filigree corner ornament"></div>

    <p class="host">VENTURE KEYSTONE</p>
    <h1 class="title title--weekend">WEEKEND</h1>
    <h1 class="title title--warm-up">WARM UP</h1>

    <div class="venue-wreath" role="img" aria-label="Watercolour wreath of green leaves"></div>
    <div class="venue-badge">
      <div class="venue-name">The<br>Lanternhouse</div>
      <div class="venue-address">482 W. Brindle Ave</div>
    </div>

    <h2 class="event-type">CLIENT APPRECIATION EVENT</h2>

    <ul class="sponsors">
      <li class="sponsor"><span class="sponsor-mark"></span>Brightvale Lighting</li>
      <li class="sponsor">Dovanti</li>
      <li class="sponsor">Hartwell Hospitality</li>
      <li class="sponsor">Quarrel &amp; Tide</li>
      <li class="sponsor">Lumora</li>
      <li class="sponsor">Marquee</li>
    </ul>
  </main>
</body>
</html>
```